Business Card Design

We need a new business card design for a company based in Larkmont, NV. We provide business consulting services in the information technology / services space. We like variations of the color blue, aqua, black, light tan, and white. Would like "cool" tones. The design should clearly communicate professionalism. Think outside the box - we don't want something "typical". Our company name is "Vantrell Advisory, LLC".
Updates

Thank you all for your submissions. We have seen some very creative and inspired designs. We have made a decision and will be moving forward with that design. Appreciate all of the hard work.

Industry/Entity Type

Information Technology

Contact Information for Business Card

Denise Harlow Trumbey
482 West Maple Ridge Dr.
Larkmont, NV 76185

```html
<!DOCTYPE html>
<html lang="en">
<head>
<meta charset="utf-8">
<title>Vantrell Advisory — Business Card</title>
<link href="https://fonts.googleapis.com/css2?family=Arimo:wght@400&display=swap" rel="stylesheet">
<style>
  :root {
    --aqua: #22c3bb;
    --aqua-deep: #14a9a2;
    --charcoal: #4a4a4a;
    --tan: #cfb08d;
    --white: #ffffff;
    --paper: #fbfbfb;
    --backdrop: #e9ecec;
  }
  * { margin: 0; padding: 0; box-sizing: border-box; }
  html, body {
    width: 1200px;
    height: 1000px;
    overflow: hidden;
    background: var(--backdrop);
    font-family: "Arimo", Arial, sans-serif;
  }
  .sheet {
    position: relative;
    width: 1200px;
    height: 1000px;
  }
  .card {
    position: absolute;
    top: 132px;
    width: 420px;
    height: 736px;
    border-radius: 4px;
    box-shadow: 0 10px 28px rgba(0, 0, 0, 0.14);
    overflow: hidden;
  }
  .card-front { left: 150px; background: var(--paper); }
  .card-back  { left: 630px; background: linear-gradient(160deg, var(--aqua) 0%, var(--aqua-deep) 100%); }

  .brand {
    position: absolute;
    top: 118px;
    right: 40px;
    display: flex;
    align-items: center;
    gap: 16px;
  }
  .brand-dot {
    width: 26px;
    height: 26px;
    border-radius: 50%;
    background: var(--aqua);
    flex: none;
  }
  .brand-name {
    color: var(--aqua);
    font-size: 34px;
    line-height: 1.05;
    font-weight: 400;
  }

  .band {
    position: absolute;
    right: 0;
    color: var(--white);
    font-size: 21px;
    line-height: 1.2;
    letter-spacing: 0.3px;
    white-space: nowrap;
  }
  .band-name {
    top: 332px;
    left: 100px;
    height: 48px;
    background: var(--aqua);
    padding: 11px 0 0 30px;
    font-size: 24px;
  }
  .band-contact {
    top: 430px;
    left: 0;
    height: 70px;
    background: var(--charcoal);
    padding: 10px 0 0 48px;
  }
  .band-address {
    top: 520px;
    left: 0;
    height: 70px;
    background: var(--tan);
    padding: 10px 0 0 48px;
  }
</style>
</head>
<body>
  <main class="sheet">
    <section class="card card-front" aria-label="Business card front">
      <div class="brand">
        <span class="brand-dot" aria-hidden="true"></span>
        <span class="brand-name">Vantrell<br>Advisory</span>
      </div>
      <div class="band band-name">Denise Harlow Trumbey</div>
      <div class="band band-contact">
        <p class="email">d.trumbey@vantrelladvisory.net</p>
        <p class="phone">555-301-0148</p>
      </div>
      <div class="band band-address">
        <p class="street">482 West Maple Ridge Dr.</p>
        <p class="city">Larkmont, NV 76185</p>
      </div>
    </section>
    <section class="card card-back" aria-label="Business card back"></section>
  </main>
</body>
</html>
```